MARLOW CREST WINE LABEL DESIGN PROJECT

We need an elegant wine label design for our new range of wine. We need 3 labels for the range

2015 MARLOW CREST SHIRAZ
2015 MARLOW CREST CABERNET SAUVIGNON
2015 MARLOW CREST CABERNET SHIRAZ

The Size is nominated at 120mm High x 90mm Wide (Front and Back) but we are open to creative expression even if size differs

We are open to any style of label and designer can work on their strengths. it can be modern/classic/old fashion etc

I have attached the marlow crest logo ( the 2 olives) and a set up called wine mandatories which is in no way a design direction just the mandatory info that needs to appear on labels. The wine mandatories is just the information that needs to go on the label it has nothing to do with the design. DO not make designs based on this at all. These labels are for red wine not olive oil.

I have also attached some of the companies current olive oil labels ( TORQUALE AND WANDELLA AND MARLOW CREST so you can see other labels and how this wine product will sit in gift baskets.

Thanks
Tomasz.

Reason: Hello Friends We have decided to extend the deadline to enable more submissions. Many of the designs submitted have images of olives and look like olive oil product. We only need the olive logo to be shown on the label but the rest of the design should be a classic simple red wine label. It is not olive oil or olive product - it is red wine. Please keep simple and stylish Thanks Tomasz

Target Market(s)

35-65

Font styles to use
Serif

Requirements
Must have
• AS per brief
Nice to have
• as per brief
Should not have
• as per brief

```html
<!DOCTYPE html>
<html lang="en">
<head>
<meta charset="utf-8">
<title>Marlow Crest Wine Labels</title>
<link rel="stylesheet" href="https://fonts.googleapis.com/css2?family=Cinzel:wght@400;600&family=Great+Vibes&display=swap">
<style>
  :root {
    --page: #efece6;
    --cream: #fbf7ea;
    --gold: #8b6b32;
    --gold-soft: #c9ad73;
    --purple: #6a3f94;
    --teal: #2e8b7d;
    --brown: #6e4f22;
    --white: #ffffff;
  }
  * { margin: 0; padding: 0; box-sizing: border-box; }
  html, body { width: 1200px; height: 900px; overflow: hidden; background: var(--page); }
  .range {
    position: relative; width: 1200px; height: 900px;
    display: flex; justify-content: center; align-items: center; gap: 90px;
  }
  .label { position: relative; width: 300px; height: 400px; font-family: "Cinzel", serif; }
  .label-shape { position: absolute; inset: 0; }
  .label--cab-shiraz { --accent: var(--purple); }
  .label--shiraz { --accent: var(--gold); }
  .label--cab-sauv { --accent: var(--teal); }
  .brand-dot {
    position: absolute; left: 141px; top: 14px; width: 18px; height: 18px;
    border-radius: 50%; background: var(--brown);
  }
  .brand-line {
    position: absolute; top: 40px; width: 100%; text-align: center;
    font-size: 8px; letter-spacing: 1.5px; color: var(--brown); font-weight: 600;
  }
  .brand-name {
    position: absolute; top: 54px; width: 100%; text-align: center;
    font-size: 22px; font-weight: 400; color: var(--gold); letter-spacing: 0.5px;
  }
  .flourish {
    position: absolute; top: 52px; width: 44px; height: 12px;
    border-radius: 6px; background: var(--gold-soft); opacity: 0.45;
  }
  .flourish--left { left: 14px; }
  .flourish--right { right: 14px; }
  .variety {
    position: absolute; top: 92px; width: 100%; text-align: center;
    font-family: "Great Vibes", cursive; font-weight: 400; font-size: 62px; line-height: 1; color: var(--accent);
  }
  .variety-sub {
    position: absolute; top: 160px; width: 100%; text-align: center;
    font-size: 14px; letter-spacing: 1px; color: var(--accent); font-weight: 600;
  }
  .grape-photo { position: absolute; left: 6px; right: 6px; top: 228px; bottom: 6px; }
  .grape-photo--blue { background: linear-gradient(160deg, #5b8d3e 0%, #3c2f63 30%, #2a2148 70%, #4b3d78 100%); }
  .grape-photo--red { background: linear-gradient(160deg, #8e2c4c 0%, #6e1f3b 50%, #a7466a 100%); }
  .grape-photo--mixed { background: linear-gradient(120deg, #cfdc98 0%, #8f9c5a 35%, #7d2a3c 70%, #b23b4c 100%); }
  .label-footer {
    position: absolute; left: 6px; right: 6px; bottom: 8px; height: 26px;
    display: flex; align-items: center; justify-content: space-between; padding: 0 8px;
    color: var(--white); font-size: 9px; letter-spacing: 0.5px;
  }
  .vintage {
    background: var(--gold); color: var(--white); font-size: 13px;
    padding: 4px 14px; font-weight: 600;
  }
  .volume { font-size: 13px; font-weight: 600; }
</style>
</head>
<body>
<main class="range">

  <article class="label label--cab-shiraz">
    <svg class="label-shape" viewBox="0 0 300 400" aria-hidden="true">
      <path d="M4,46 Q24,46 24,26 Q150,-12 276,26 Q276,46 296,46 L296,396 L4,396 Z" fill="var(--cream)" stroke="var(--purple)" stroke-width="4"/>
    </svg>
    <div class="grape-photo grape-photo--blue" role="img" aria-label="Photograph of dark blue grapes with a vine leaf"></div>
    <span class="brand-dot"></span>
    <p class="brand-line">THE MARLOW CREST,</p>
    <div class="flourish flourish--left" role="img" aria-label="Gold corner flourish"></div>
    <div class="flourish flourish--right" role="img" aria-label="Gold corner flourish"></div>
    <h2 class="brand-name">MARLOW CREST</h2>
    <h1 class="variety">Cabernet</h1>
    <p class="variety-sub">SHIRAZ</p>
    <div class="label-footer"><span>14.5% ALC/VOL</span><span class="vintage">2015</span><span class="volume">750ML</span></div>
  </article>

  <article class="label label--shiraz">
    <svg class="label-shape" viewBox="0 0 300 400" aria-hidden="true">
      <path d="M4,46 Q24,46 24,26 Q150,-12 276,26 Q276,46 296,46 L296,396 L4,396 Z" fill="var(--cream)" stroke="var(--gold)" stroke-width="4"/>
    </svg>
    <div class="grape-photo grape-photo--red" role="img" aria-label="Photograph of red grapes"></div>
    <span class="brand-dot"></span>
    <p class="brand-line">THE MARLOW CREST,</p>
    <div class="flourish flourish--left" role="img" aria-label="Gold corner flourish"></div>
    <div class="flourish flourish--right" role="img" aria-label="Gold corner flourish"></div>
    <h2 class="brand-name">MARLOW CREST</h2>
    <h1 class="variety">Shiraz</h1>
    <div class="label-footer"><span>14.5% ALC/VOL</span><span class="vintage">2015</span><span class="volume">750ML</span></div>
  </article>

  <article class="label label--cab-sauv">
    <svg class="label-shape" viewBox="0 0 300 400" aria-hidden="true">
      <path d="M4,46 Q24,46 24,26 Q150,-12 276,26 Q276,46 296,46 L296,396 L4,396 Z" fill="var(--cream)" stroke="var(--teal)" stroke-width="4"/>
    </svg>
    <div class="grape-photo grape-photo--mixed" role="img" aria-label="Photograph of green and red grapes"></div>
    <span class="brand-dot"></span>
    <p class="brand-line">THE MARLOW CREST,</p>
    <div class="flourish flourish--left" role="img" aria-label="Gold corner flourish"></div>
    <div class="flourish flourish--right" role="img" aria-label="Gold corner flourish"></div>
    <h2 class="brand-name">MARLOW CREST</h2>
    <h1 class="variety">Cabernet</h1>
    <p class="variety-sub">SAUVIGNON</p>
    <div class="label-footer"><span>14.5% ALC/VOL</span><span class="vintage">2015</span><span class="volume">750ML</span></div>
  </article>

</main>
</body>
</html>
```